Develop new wine label for entry level Greek wines **

We need a label design for the new line of entry level Greek wines.

We will have 4 SKU: red dry wine, red semi sweet wine, white dry wine, white semi-sweet wines.

We would like to see traditional greek houses on it.

There needs to be a slight colour difference between dry and semi sweet wines (you can maybe change colours of some details in order to differentiate wines on the shelf).

We would like to use designs that use white and blue colours (I attached some images for your inspiration). The glass bottle will be transparent so keep in mind how the label will coordinate with the colour of the wine itself.

The label needs to communicate that the wine is from Greece, this wine is simple, approachable, easy to drink, modern and fun.

The brand name is the ancient Greek word "kelvo". Quoting knowlark: " Kelvo (ancient Greek: κἐλβος, plural: κἐλβοι; English prefix: eco- for ecology and economics) refers to three related but distinct concepts: the family, the family's property, and the house.".

So feel free to further elaborate on the concept.

The text that should appear on the label:
1. Brand name - Kelvo (a good idea would be to use a greek style shrift would be great to mimic greek letters κέλβος).
2. White semi-sweet / White dry / Red semi-sweet / Red dry

Target Market(s)

Ukraine

Font styles to use
Serif

Colors
33a6d7
cee9f5
ffffff
e34297

Requirements
Must have
• The customer needs to look at the bottle and understand that is it from Greece straight away.

```html
<!DOCTYPE html>
<html lang="en">
<head>
<meta charset="utf-8">
<title>Kelvo wine labels</title>
<link rel="stylesheet" href="https://fonts.googleapis.com/css2?family=Cormorant+SC:wght@500;600&display=swap">
<style>
  :root {
    --page: #ffffff;
    --sky-light: #bcd0dc;
    --sky-dot: #aec6d6;
    --aegean: #7f9fd3;
    --aegean-mid: #7a9fc5;
    --coral: #eca492;
    --band: #1f5ba8;
    --ink: #1b2a5c;
    --houses: #f3f6fa;
  }
  html, body {
    margin: 0;
    width: 884px;
    height: 1200px;
    overflow: hidden;
    background: var(--page);
  }
  .label-row {
    position: absolute;
    top: 352px;
    left: 0;
    width: 884px;
    display: flex;
    justify-content: center;
    gap: 44px;
  }
  .wine-label {
    width: 380px;
    height: 495px;
    display: block;
  }
  .variant-name,
  .brand-name {
    font-family: "Cormorant SC", "Times New Roman", serif;
    fill: var(--ink);
  }
  .variant-name { font-weight: 600; }
  .brand-name { font-weight: 600; letter-spacing: 1px; }
</style>
</head>
<body>
<main class="label-row">

  <!-- Red dry -->
  <svg class="wine-label label-dry" viewBox="0 0 248 323" aria-label="Kelvo Red Dry label">
    <defs><clipPath id="clip-dry"><rect width="248" height="323"/></clipPath></defs>
    <g clip-path="url(#clip-dry)">
      <rect width="248" height="323" fill="var(--aegean)"/>
      <circle cx="255" cy="55" r="125" fill="var(--sky-light)"/>
      <path d="M0 150 Q120 130 248 175 L248 323 L0 323 Z" fill="var(--sky-light)"/>
      <circle cx="55" cy="305" r="100" fill="var(--sky-dot)" role="img" aria-label="Dotted pattern area"/>
      <circle cx="235" cy="292" r="100" fill="var(--aegean)"/>
      <rect x="32" y="30" width="196" height="196" rx="6" fill="var(--houses)" role="img" aria-label="Illustration of white Greek island houses with blue domes and trees"/>
      <rect y="309" width="248" height="14" fill="var(--band)"/>
    </g>
    <text class="variant-name" x="150" y="40" font-size="22">Red Dry</text>
    <text class="brand-name" x="143" y="286" font-size="32">KELVO</text>
  </svg>

  <!-- Red semi-sweet -->
  <svg class="wine-label label-semi" viewBox="0 0 248 323" aria-label="Kelvo Red Semi-Sweet label">
    <defs><clipPath id="clip-semi"><rect width="248" height="323"/></clipPath></defs>
    <g clip-path="url(#clip-semi)">
      <rect width="248" height="323" fill="var(--coral)"/>
      <circle cx="255" cy="55" r="125" fill="var(--sky-light)"/>
      <path d="M0 140 Q120 125 248 160 L248 323 L0 323 Z" fill="var(--aegean-mid)"/>
      <path d="M0 210 Q120 190 248 215 L248 323 L0 323 Z" fill="var(--sky-light)"/>
      <circle cx="55" cy="305" r="100" fill="var(--sky-dot)" role="img" aria-label="Dotted pattern area"/>
      <circle cx="235" cy="292" r="100" fill="var(--coral)"/>
      <rect x="32" y="30" width="196" height="196" rx="6" fill="var(--houses)" role="img" aria-label="Illustration of white Greek island houses with blue domes and trees"/>
      <rect y="309" width="248" height="14" fill="var(--band)"/>
    </g>
    <text class="variant-name" x="162" y="36" font-size="22">Red</text>
    <text class="variant-name" x="162" y="55" font-size="12">Semi-Swett</text>
    <text class="brand-name" x="143" y="286" font-size="32">KELVO</text>
  </svg>

</main>
</body>
</html>
```